Flyer für ambulante und teilstationäre Pflege
Zielgruppe
ambulante und teilstationäre Pflege
Zielgruppe: Pflegebedürftige Menschen, die noch ausreichend mobil sind, um als Gast in unserer Tagespflege zu sein
Aufgabenstellung
Standard DIN lang Format
Stil soll unserer Homepage folgen: www.pflegeteam-sonnhalde.de
Wir achten immer sehr darauf, nicht so einen verstaubten Stil wie viele andere Pflegeeinrichtungen zu haben, sondern fröhlich, bunt , ansprechend

```html
<!DOCTYPE html>
<html lang="de">
<head>
<meta charset="utf-8">
<title>Tagespflege Sonnhalde – Flyer</title>
<link href="https://fonts.googleapis.com/css2?family=Jost:wght@300;400;500;600&display=swap" rel="stylesheet">
<style>
  :root {
    --teal: #0099a0;
    --white: #ffffff;
    --ink: #111111;
    --grey: #4d4d4f;
  }
  * { margin: 0; padding: 0; box-sizing: border-box; }
  html, body { width: 1200px; height: 1166px; overflow: hidden; background: var(--white); }
  body { position: relative; font-family: "Jost", sans-serif; color: var(--white); }

  .panel { position: absolute; background: var(--teal); }
  .panel--left { left: 0; top: 0; width: 583px; height: 1031px; }
  .panel--right { left: 617px; top: 0; width: 583px; height: 969px; }

  .photo {
    position: absolute;
    border-radius: 50%;
    border: 19px solid var(--white);
    box-shadow: 0 4px 10px rgba(0,0,0,0.18);
  }
  .photo--reading {
    left: 80px; top: -12px; width: 516px; height: 516px;
    background: radial-gradient(circle at 60% 40%, #f4eee8 0%, #d9c6c2 45%, #8e7c7a 100%);
  }
  .photo--bench {
    left: 606px; top: -24px; width: 516px; height: 516px;
    background: linear-gradient(180deg, #c9d4dc 0%, #9aa79a 40%, #5d6b4d 70%, #b8a88a 100%);
  }

  .headline {
    position: absolute; left: 0; width: 583px; top: 608px;
    text-align: center; font-weight: 500; font-size: 88px; line-height: 92px;
    letter-spacing: 0.5px;
  }
  .tagline {
    position: absolute; left: 0; width: 583px; top: 868px;
    text-align: center; font-weight: 400; font-size: 50px; line-height: 1;
  }
  .tagline strong { font-weight: 600; }

  .value { position: absolute; line-height: 1; white-space: nowrap; }
  .value--atmosphere { right: 33px; top: 510px; font-size: 46px; font-weight: 600; }
  .value--attention { left: 641px; top: 583px; font-size: 46px; font-weight: 300; }
  .value--satisfaction { right: 21px; top: 650px; font-size: 64px; font-weight: 400; }
  .value--everyday { left: 771px; top: 742px; font-size: 46px; font-weight: 600; }
  .value--gratitude { left: 672px; top: 815px; font-size: 64px; font-weight: 400; }
  .value--together { right: 43px; top: 896px; font-size: 46px; font-weight: 600; }

  .contact {
    position: absolute; left: 617px; width: 583px; top: 987px;
    text-align: center; color: var(--ink);
  }
  .contact__claim { color: var(--teal); font-size: 31px; font-weight: 500; line-height: 1; margin-bottom: 12px; }
  .contact__line { font-size: 21px; font-weight: 500; line-height: 33px; }
  .contact__label { color: var(--teal); font-weight: 400; }
  .contact__web { color: var(--teal); font-weight: 500; }

  .brand {
    position: absolute; left: 52px; top: 1060px;
    display: flex; align-items: center; gap: 14px;
  }
  .brand__name {
    color: var(--grey); font-weight: 400; font-size: 34px; line-height: 1;
    letter-spacing: 1px; text-align: right;
  }
  .brand__name small { display: block; font-size: 22px; margin-top: 8px; letter-spacing: 1px; }
  .brand__dot { width: 78px; height: 78px; border-radius: 50%; background: var(--teal); }
</style>
</head>
<body>
  <div class="panel panel--left"></div>
  <div class="panel panel--right"></div>

  <div class="photo photo--reading" role="img" aria-label="Pflegerin liest einer lachenden Seniorin aus einem Buch vor"></div>
  <div class="photo photo--bench" role="img" aria-label="Senioren und Betreuerinnen sitzen fröhlich auf einer Parkbank und schauen auf ein Tablet"></div>

  <h1 class="headline">Von MENSCH<br>zu MENSCH</h1>
  <p class="tagline">Wir <strong>lieben</strong> Pflege</p>

  <p class="value value--atmosphere">Familiäre Atmosphäre</p>
  <p class="value value--attention">Liebevolle Zuwendung</p>
  <p class="value value--satisfaction">Zufriedenheit</p>
  <p class="value value--everyday">Bunter Alltag</p>
  <p class="value value--gratitude">Dankbarkeit</p>
  <p class="value value--together">Zusammenhalt</p>

  <div class="contact">
    <p class="contact__claim">Pflegeprofis seit 1994</p>
    <p class="contact__line"><span class="contact__label">Telefon:</span> 0431 12 34 56 70</p>
    <p class="contact__line"><span class="contact__label">E-Mail:</span> info@pflegeteam-sonnhalde.de</p>
    <p class="contact__line"><span class="contact__label">Adresse:</span> Lindenweg 12, 24999 Musterhagen</p>
    <p class="contact__line contact__web">www.pflegeteam-sonnhalde.de</p>
  </div>

  <div class="brand">
    <p class="brand__name">TAGESPFLEGE SONNHALDE<small>MUSTERHAGEN</small></p>
    <div class="brand__dot"></div>
  </div>
</body>
</html>
```